New Business Card Design Project

Want a simple but attention grabbing business card. Back Side having mainly our logo and basic info-the front side a typical business card.

Contact Information for Business Card

Hearth & Tile Interiors
218 NW Larkspur Rd. Suite 207
Ankeny, Iowa 50021

phone- 515.482.7093

website is -htidesigns.com

```html
<!DOCTYPE html>
<html lang="en">
<head>
<meta charset="utf-8">
<title>Hearth &amp; Tile Interiors — Business Card</title>
<link rel="stylesheet" href="https://fonts.googleapis.com/css2?family=Montserrat:wght@400;500;700;800&display=swap">
<style>
  :root {
    --bg: #1c1d22;
    --card: #0b1428;
    --orange: #e8581f;
    --blue: #2b73c2;
    --white: #f2f4f7;
    --silver: #b9bcc2;
  }
  * { box-sizing: border-box; margin: 0; padding: 0; }
  html, body { width: 1200px; height: 953px; overflow: hidden; }
  body {
    background: var(--bg);
    font-family: "Montserrat", sans-serif;
    display: flex;
    align-items: center;
    justify-content: center;
    gap: 40px;
  }
  .card {
    width: 540px;
    height: 330px;
    background: var(--card);
    border-radius: 24px;
    position: relative;
    box-shadow: 0 12px 30px rgba(0,0,0,.5);
    overflow: hidden;
  }
  .card-back {
    display: flex;
    align-items: center;
    justify-content: center;
  }
  .brand-mark {
    font-weight: 800;
    color: var(--silver);
    font-size: 34px;
    letter-spacing: .5px;
    text-align: center;
    line-height: 1.2;
  }
  .card-front .brand-mark {
    position: absolute;
    top: 48px;
    left: 0;
    right: 0;
    color: var(--orange);
    font-size: 26px;
  }
  .details {
    position: absolute;
    top: 140px;
    left: 0;
    right: 0;
    display: flex;
    justify-content: center;
    align-items: center;
    gap: 22px;
  }
  .person { text-align: right; }
  .person-name {
    color: var(--orange);
    font-weight: 700;
    font-size: 21px;
    letter-spacing: .3px;
  }
  .person-title {
    color: var(--white);
    font-size: 14px;
    font-weight: 500;
    margin-top: 4px;
  }
  .divider {
    width: 2px;
    height: 74px;
    background: var(--blue);
  }
  .contacts { list-style: none; }
  .contacts li {
    color: var(--white);
    font-size: 13px;
    font-weight: 500;
    display: flex;
    align-items: center;
    gap: 8px;
    line-height: 1.75;
  }
  .contacts svg { width: 12px; height: 12px; flex: none; }
  .address-row {
    position: absolute;
    bottom: 48px;
    left: 30px;
    right: 30px;
    display: flex;
    align-items: center;
    gap: 12px;
  }
  .rule { flex: 1; height: 2px; background: var(--orange); }
  .address {
    color: var(--white);
    font-size: 13px;
    font-weight: 500;
    white-space: nowrap;
  }
</style>
</head>
<body>
  <section class="card card-back">
    <div class="brand-mark">Hearth &amp; Tile<br>Interiors</div>
  </section>

  <section class="card card-front">
    <div class="brand-mark">Hearth &amp; Tile Interiors</div>

    <div class="details">
      <div class="person">
        <div class="person-name">DANA WHITFIELD</div>
        <div class="person-title">CEO &amp; Founder</div>
      </div>
      <div class="divider"></div>
      <ul class="contacts">
        <li>
          <svg viewBox="0 0 12 12" aria-hidden="true"><path fill="#e8581f" d="M2.5 1l2 2-1 1.2c.6 1.4 1.9 2.7 3.3 3.3l1.2-1 2 2-1.2 1.5C5.5 10 2 6.5 1 2.2z"/></svg>
          515.482.7093
        </li>
        <li>
          <svg viewBox="0 0 12 12" aria-hidden="true"><rect x="1" y="2.5" width="10" height="7" fill="#e8581f"/><path d="M1 2.8l5 3.6 5-3.6" stroke="#0b1428" stroke-width="1" fill="none"/></svg>
          info@htidesigns.com
        </li>
        <li>
          <svg viewBox="0 0 12 12" aria-hidden="true"><circle cx="6" cy="6" r="5" fill="#e8581f"/><path d="M1 6h10M6 1c2 2.5 2 7.5 0 10M6 1c-2 2.5-2 7.5 0 10" stroke="#0b1428" stroke-width=".8" fill="none"/></svg>
          htidesigns.com
        </li>
      </ul>
    </div>

    <div class="address-row">
      <span class="rule"></span>
      <span class="address">218 NW Larkspur Rd. Suite 207, Ankeny, Iowa 50021</span>
      <span class="rule"></span>
    </div>
  </section>
</body>
</html>
```